Letterhead for a busy but slightly unconventional doctor

I need a letterhead for a busy and senior London based medical doctor who specialises in psychiatry.
Letterhead needs to say
Dr Lena Morwen Ostrow MA PhD MRCP MRCPsych
BPR number 3819057
17, Calloway Street
London N4K 2TB
Telephone: 07812 430276
Email: lena.m.ostrow@dovrel.ac.uk
Letterhead needs to be greyscale or black and white. I would like a classic but contemporary look but a bit quirky/unusual.
I will print on pale grey paper so needs to look good with that.
Something a little bit unconventional.
other doctors and patients
Doctor

```html
<!DOCTYPE html>
<html lang="en">
<head>
<meta charset="utf-8">
<title>Letterhead – Dr Lena Morwen Ostrow</title>
<link rel="stylesheet" href="https://fonts.googleapis.com/css2?family=Open+Sans:wght@300;400;600&family=Crimson+Pro:wght@400&display=swap">
<style>
  :root {
    --paper: #ffffff;
    --ink: #1e1e1e;
    --ink-soft: #3a3a3a;
    --rule: #555555;
  }
  html, body {
    margin: 0;
    padding: 0;
    overflow: hidden;
    background: var(--paper);
  }
  .letterhead {
    position: relative;
    width: 849px;
    height: 1200px;
    background: var(--paper);
    color: var(--ink);
    overflow: hidden;
  }
  .sender {
    position: absolute;
    left: 28px;
    top: 20px;
    width: 225px;
    font-family: "Open Sans", sans-serif;
  }
  .sender-name {
    margin: 0;
    font-size: 16px;
    font-weight: 600;
    letter-spacing: 0.01em;
    line-height: 20px;
  }
  .sender-titles {
    margin: 0 0 8px;
    font-size: 11.5px;
    font-weight: 400;
    letter-spacing: 0.04em;
    line-height: 16px;
  }
  .sender-rule {
    display: block;
    width: 225px;
    height: 2px;
    margin-bottom: 10px;
  }
  .sender-details {
    margin: 0;
    font-style: normal;
    font-family: "Crimson Pro", serif;
    font-size: 11.5px;
    line-height: 14.5px;
    color: var(--ink-soft);
  }
  .letter {
    position: absolute;
    left: 277px;
    top: 276px;
    width: 488px;
  }
  .letter-heading {
    margin: 0 0 22px;
    font-family: "Open Sans", sans-serif;
    font-weight: 300;
    font-size: 29px;
    line-height: 34px;
    color: var(--ink);
  }
  .letter-body p {
    margin: 0 0 17px;
    font-family: "Crimson Pro", serif;
    font-size: 14.2px;
    line-height: 17.4px;
    text-align: justify;
    hyphens: auto;
    color: var(--ink);
  }
  .signoff {
    position: absolute;
    left: 277px;
    top: 990px;
    width: 488px;
    display: flex;
    align-items: flex-end;
    justify-content: space-between;
    font-family: "Crimson Pro", serif;
    font-size: 14.2px;
    line-height: 18px;
  }
  .signature-line {
    display: block;
    width: 228px;
    height: 2px;
    margin-bottom: 3px;
  }
</style>
</head>
<body>
<main class="letterhead">
  <header class="sender">
    <h1 class="sender-name">Dr Lena Morwen Ostrow</h1>
    <p class="sender-titles">MA PhD MRCP MRCPsych</p>
    <svg class="sender-rule" viewBox="0 0 225 2" aria-hidden="true">
      <line x1="1" y1="1" x2="225" y2="1" stroke="var(--rule)" stroke-width="1.4" stroke-dasharray="1.5 2.2" stroke-linecap="round"/>
    </svg>
    <address class="sender-details">
      BPR number 3819057<br>
      17, Calloway Street<br>
      London N4K 2TB<br>
      t: 07812 430276<br>
      e: lena.m.ostrow@dovrel.ac.uk
    </address>
  </header>

  <section class="letter">
    <h2 class="letter-heading">Sample text</h2>
    <div class="letter-body">
      <p>Facepersped inci aut entiur alit que inullabora quiam doluptionse simentii orepudion consed utae doluttatet quid eat.</p>
      <p>Nullore rorenih illigenia monet, acerendaepro consenum quae con eum corro excerit mos ratectatium que in plandita qui ilia consereprrum voluptia voluptatur audaepedi ipsam quunt excipsundem aut ex conectus aut modi denim faciae volecatem ipid minienda aborest aliqui dest, vero doluptat. Osandis nimus aut quam, sequi dolorem faccus arum fugiae nos solupta temquis maximus ea cum ratem velendae nonsequi dolorum esto moditae volorem rerum, omnim eos eatus vel ipsam nobis aut que nimus et vendae pernatem quibusa. Ut officatur sitatem aut rem lam, cus dolupta quiae nis et que re voluptur.</p>
      <p>Mus aliquiments endunt qui aut esto excepererro ipsamus rem dolorem aut aut harum il ium nis abo. Equod molor anda aut modit, post simodi doluptat exped moluptia que natumquam dolutas rent que sunt et ma comnihicilit proratquam veloria nonsequatem que etur? Quiscilique none pa dollaut estetur! Igniture cores vendit doluptas nihillore nonsequat faccum fugitas reium et, saeseium mus sit maio te volest, ad ut ullitiorest esquo mo ipsunt, cuptatur aped ut odicitis sam experro bla niet, conse velecto tatiaeciae libus il il moluptati tem faccus, que sus cum quis aut hicitatur acepreitis abor arum aliciquunt eos mintius magnatem eum ut que porestior sae volesti oriscae. Porchil ignis id quae explamus vero ium ipiciat es eumet, sedi sincimagni nonsequam quaspici reritatiur?</p>
      <p>Ga. Et quiscia scienih el duntus volecus et omnisinim aspita sunt omnolori cor sequi offici beatchit rem faceptio voluptat la seque cus enti occum id quate laudaepudit quidunten et quiatque omnis quia veliqui Edis volest essintiurist inam quae liquide llendam, officia sita pratium daecearum, quuntur molor sae core pro berenquis que doluptaque endit aut eos autem eaquidi atistius ma nat landissum vit eum qui audit.</p>
    </div>
  </section>

  <footer class="signoff">
    <span class="place-date">London, 10/23/2015</span>
    <svg class="signature-line" viewBox="0 0 228 2" aria-hidden="true">
      <line x1="0" y1="1" x2="228" y2="1" stroke="var(--rule)" stroke-width="1" stroke-dasharray="1 1.6"/>
    </svg>
  </footer>
</main>
</body>
</html>
```